BARRIER BANNER KTV

I am looking for a visual for a banner
3 meters long by 1 high.
In the same theme as the visual identity of the company.
As simple as possible without overloading

There must be the LOGO, the title VOLTARIS SERVICES TECHNIQUES

_________________________

I am looking for a visual for a banner (barrier banner)
3 meters long by 1 high.

AIR CONDITIONING HEATING VENTILATION
04 52 31 69 14

Font styles to use
Sans Serif

Colors
33b8a4
00a990
33a6d7
0493ce
3176b5
0355a3
ffffff

Requirements
Should not have
• No photo
No photo

```html
<!DOCTYPE html>
<html lang="fr">
<head>
<meta charset="utf-8">
<title>KTV – Barrier Banner</title>
<link href="https://fonts.googleapis.com/css2?family=Montserrat:wght@800;900&display=swap" rel="stylesheet">
<style>
  :root {
    --teal: #00a990;
    --teal-soft: #33b8a4;
    --sky: #33a6d7;
    --azure: #0493ce;
    --blue: #3176b5;
    --navy: #0355a3;
    --white: #ffffff;
    --accent-glow: rgba(94, 203, 242, 0.55);
    --page: #ffffff;
  }
  * { margin: 0; padding: 0; box-sizing: border-box; }
  html, body {
    width: 1200px;
    height: 800px;
    overflow: hidden;
    background: var(--page);
  }
  .canvas {
    position: relative;
    width: 1200px;
    height: 800px;
  }
  .banner {
    position: absolute;
    left: 30px;
    top: 204px;
    width: 1140px;
    height: 392px;
    border-radius: 30px 30px 0 0;
    overflow: hidden;
    background: linear-gradient(90deg, var(--teal) 0%, var(--teal-soft) 18%, var(--azure) 50%, var(--blue) 78%, var(--navy) 100%);
    font-family: "Montserrat", sans-serif;
    color: var(--white);
    text-align: center;
  }
  .banner__accent {
    position: absolute;
    top: 0;
    width: 300px;
    height: 280px;
  }
  .banner__accent--left {
    left: 0;
    background: radial-gradient(ellipse at 20% 30%, var(--accent-glow) 0%, rgba(94, 203, 242, 0) 70%);
  }
  .banner__accent--right {
    right: 0;
    background: radial-gradient(ellipse at 80% 30%, var(--accent-glow) 0%, rgba(94, 203, 242, 0) 70%);
  }
  .brand-name {
    position: absolute;
    left: 0;
    right: 0;
    top: 6px;
    font-size: 200px;
    font-weight: 900;
    line-height: 1;
    letter-spacing: 6px;
  }
  .tagline {
    position: absolute;
    left: 0;
    right: 0;
    font-weight: 800;
    line-height: 1;
    text-shadow: 0 2px 4px rgba(0, 40, 80, 0.35);
  }
  .tagline--company { top: 224px; font-size: 37px; }
  .tagline--services { top: 266px; font-size: 37px; }
  .phone {
    position: absolute;
    left: 0;
    right: 0;
    top: 318px;
    font-size: 68px;
    font-weight: 800;
    line-height: 1;
    letter-spacing: 2px;
    text-shadow: 0 2px 4px rgba(0, 40, 80, 0.35);
  }
</style>
</head>
<body>
<main class="canvas">
  <section class="banner">
    <div class="banner__accent banner__accent--left" role="img" aria-label="Decorative light-blue diagonal accents"></div>
    <div class="banner__accent banner__accent--right" role="img" aria-label="Decorative light-blue diagonal accents"></div>
    <div class="brand-name">KTV</div>
    <p class="tagline tagline--company">VOLTARIS SERVICES TECHNIQUES</p>
    <p class="tagline tagline--services">AIR CONDITIONING HEATING VENTILATION</p>
    <p class="phone">04 52 31 69 14</p>
  </section>
</main>
</body>
</html>
```